Deliver a professional and engaging investment propsal.

I am appealing to highend smart investors and need a high quality, engaging and formal presentation in PDF.
StowBin: https://www.stowbin.net/sh/qwmtr48kelvan2x/ZZTrPHmLe7WqsnBFjQ4kR8vYt?dl=0
Text for project is in Stowbin called New Proposal Final
Along with past much older attempts of this job.
Any additional ideas to enable a better outcome would be appreicated.

```html
<!DOCTYPE html>
<html lang="en">
<head>
<meta charset="utf-8">
<title>Ridgeline Town Center – Project Proposal</title>
<link href="https://fonts.googleapis.com/css2?family=Lato:ital,wght@0,400;0,700;0,900;1,400&display=swap" rel="stylesheet">
<style>
:root{
  --backdrop:#8e8f93;
  --paper:#f7f8fb;
  --navy:#1c2f6b;
  --navy-deep:#14244f;
  --band:#4d6190;
  --band-soft:#c9d0de;
  --title:#1d3470;
  --body:#4a4d55;
  --table:#2d5ca8;
  --table-alt:#2a549b;
  --table-head:#3a6bb8;
}
*{box-sizing:border-box;margin:0;padding:0}
html,body{width:1200px;height:1200px;overflow:hidden;background:var(--backdrop);font-family:"Lato",sans-serif}
.board{position:relative;width:1200px;height:1200px}
.page{position:absolute;width:270px;height:378px;background:var(--paper);box-shadow:3px 4px 6px rgba(0,0,0,.35);overflow:hidden}
.page .bands{position:absolute;inset:0;width:100%;height:100%}
.page-title{position:absolute;left:24px;top:20px;font-size:16.5px;font-weight:700;color:var(--title);line-height:1.1}
.p{font-size:3.9px;line-height:1.4;color:var(--body);margin-bottom:5px}
.col{position:absolute}
.subhead{font-size:5.2px;font-weight:700;color:var(--title);margin:4px 0}
.fill{position:absolute}
.row1{top:163px}.row2{top:658px}
.c1{left:38px}.c2{left:326px}.c3{left:613px}.c4{left:900px}

/* cover */
.cover-panel{position:absolute;left:23px;top:24px;width:224px;height:330px;background:linear-gradient(170deg,#2f5fb4 0%,#3f6cbc 35%,#2a3f70 60%,#3b2f2c 85%,#5a4438 100%)}
.cover-brand{position:absolute;left:10px;top:22px;display:flex;align-items:center;gap:5px;color:#fff;font-size:10.5px;font-weight:900;letter-spacing:.3px}
.cover-brand i{display:block;width:8px;height:8px;background:#fff;border-radius:50%}
.cover-tag{position:absolute;right:18px;top:18px;color:#fff;font-weight:900;font-size:10.5px;line-height:1.25}
.cover-name{position:absolute;left:20px;bottom:22px;color:#fff}
.cover-name h1{font-size:15px;font-weight:400;letter-spacing:.2px}
.cover-name p{font-size:8.6px;margin-top:2px;letter-spacing:.3px}

/* table */
.sens{position:absolute;left:26px;top:161px;width:218px;border-collapse:collapse;font-size:3.8px;color:#fff}
.sens td,.sens th{padding:0 3px;height:10.1px;border-bottom:.6px solid #5b84c6;text-align:left;font-weight:400}
.sens th{background:var(--table-head)}
.sens tr:nth-child(odd) td{background:var(--table)}
.sens tr:nth-child(even) td{background:var(--table-alt)}

.contact{position:absolute;left:32px;top:257px;width:206px;height:50px;border-radius:9px;background:var(--navy-deep);color:#fff;font-size:4.3px;text-align:center;line-height:1.5;padding-top:8px}
.contact em{font-style:italic}
</style>
</head>
<body>
<main class="board">

  <!-- Page 1: cover -->
  <section class="page row1 c1">
    <svg class="bands" viewBox="0 0 270 378" aria-hidden="true"><polygon points="0,355 0,300 270,100 270,150 0,378" fill="var(--navy-deep)"/></svg>
    <div class="cover-panel" role="img" aria-label="Photograph of a modern hotel building at dusk">
      <div class="cover-brand"><i></i>MERIDIAN CAPITAL</div>
      <div class="cover-tag">PROJECT<br>PROPOSAL</div>
      <div class="cover-name"><h1>RIDGELINE TOWN CENTER</h1><p>60 ACRE MIXED-USE DEVELOPMENT</p></div>
    </div>
  </section>

  <!-- Page 2: proposal -->
  <section class="page row1 c2">
    <svg class="bands" viewBox="0 0 270 378" aria-hidden="true"><polygon points="270,95 270,378 245,378 245,105" fill="var(--band)"/><polygon points="0,300 0,378 60,378" fill="var(--band-soft)" opacity=".5"/></svg>
    <h2 class="page-title" style="top:22px">Proposal</h2>
    <div class="fill" role="img" aria-label="Site plan drawing of the development lots marked sold" style="left:25px;top:44px;width:101px;height:113px;background:linear-gradient(135deg,#b9bfb3,#d8dbd2 50%,#9aa79a)"></div>
    <div class="col" style="left:133px;top:57px;width:110px">
      <p class="p">We have an incredible property at 1180 Prairie Route 9, Ridgeline, North Dakota 58000 which we have fully funded with cash and now need a joint venture partner, buyer or lender to get this project to completion and producing a substantial profit we all can share.</p>
      <p class="p">Our property is located on the best oil reserves in the world in North Dakota with more oil than any other county in the basin and with the lowest recovery cost.</p>
      <p class="p">We own the property and need a partner to develop the site and bring to the market at half the cost of competitors.</p>
    </div>
    <div class="col" style="left:25px;top:164px;width:218px">
      <div class="subhead">Participation Options</div>
      <p class="p">A joint venture partner would support all the costs developing the property without the upfront costs of the property purchase.</p>
      <p class="p">All sales would be split to ensure both parties are paid out in such a way that both are paid out in full at the same time then a 50/50 profit share split on all remaining sales.</p>
      <p class="p">Contract drawn up protecting and supporting both parties on agreed terms.</p>
      <p class="p">As a potential joint venture partner, I would cover the full property (57.7 acres) cost as mentioned of $124,784 per acre (57.7 acres) ($7,200,000)</p>
      <p class="p">Joint venture partner to supply the development costs estimated to be around $65,000 an acre estimated pending tender selection and additional refundable security bonds held with the city on development works.</p>
      <p class="p">Development costs could be in up to three stages to lower outlay and limit exposure if so desired, however it will take longer to complete and bring to market.</p>
      <p class="p">A buyer can be fully supported by myself to oversee the full project and outcomes and support the budgets of construction and sales to get the highest returns for a small fee.</p>
      <p class="p">To purchase the property, you would need to contact me directly and I can introduce you to our realtor who will discount his commission from 6% to 5% which is a significant saving.</p>
      <p class="p">Financing on excellent terms allowing 12 to 18 months for income streams and could be linked to a joint venture option / profit share.</p>
    </div>
  </section>

  <!-- Page 3: major site changes -->
  <section class="page row1 c3">
    <svg class="bands" viewBox="0 0 270 378" aria-hidden="true"><polygon points="0,220 0,378 20,378 20,210" fill="var(--band)"/><polygon points="0,250 270,170 270,300 0,378" fill="var(--band-soft)" opacity=".35"/></svg>
    <h2 class="page-title">Major Site Changes</h2>
    <div class="fill" role="img" aria-label="Aerial photograph of the development site beside the highway" style="left:22px;top:49px;width:113px;height:110px;background:linear-gradient(160deg,#9c8a7c,#b6a597 45%,#8a7a70 75%,#c6c0bb)"></div>
    <div class="col" style="left:141px;top:50px;width:108px">
      <p class="p">We purchased the property in 2013 for cash and without any additional debt, at the time we had highway 85 frontage just outside city limits.</p>
      <p class="p">2014 site zoning changed allowing a commercial zoning.</p>
      <p class="p">Flag Hotel site purchased 2014 now with the option to purchase the franchise license and build the hotel ourselves.</p>
      <p class="p">In 2016 we were added into City Limits which was a massive improvement to our site now taking advantage of confirmed city water and sewer was a great outcome.</p>
      <p class="p">In 2016 the new bypass opened intersecting our highway frontage just 100 yards away which brings all the traffic right past our site which was a massive win for this project.</p>
    </div>
    <div class="col" style="left:25px;top:196px;width:222px">
      <p class="p">Same commercial property listed across the road at $750,000 per acre retail at Harbor Commons and other business parks average listings $550,00 per acre.</p>
      <p class="p">In late 2017 we applied for full site development application and were approved in mid-2018 which again was a significant improvement to the project.</p>
      <p class="p">May 2018 Full site infrastructure development approval which includes all roads and city services, this will trigger interest in the site from passing traffic and with a great marketing campaign will surely start sales coming in quickly once we break ground and start work.</p>
      <p class="p">We also can buy the franchise license of the Northstar hotel for additional income potential if desired.</p>
    </div>
  </section>

  <!-- Page 4: location -->
  <section class="page row1 c4">
    <svg class="bands" viewBox="0 0 270 378" aria-hidden="true"><polygon points="270,110 270,378 250,378 250,120" fill="var(--band)"/><polygon points="0,280 0,378 30,378" fill="var(--band-soft)" opacity=".5"/></svg>
    <h2 class="page-title">Location</h2>
    <div class="fill" role="img" aria-label="Site plan drawing of the lots with sold markers" style="left:25px;top:51px;width:121px;height:151px;background:linear-gradient(135deg,#aab5a6,#d5d9cf 50%,#9aa99a)"></div>
    <div class="col" style="left:154px;top:51px;width:93px">
      <p class="p">Our property is ideally located in the city, United States of America, despite its humble beginnings, has suddenly found itself at the epicentre of the oil boom. Located in Western North Dakota the city has seen workers flood into the area over recent years to fill positions to support the growth.</p>
      <p class="p">The County has more recoverable oil and gas at the lowest recoverable cost per barrel at $24, making it most affordable anywhere in the basin, centrally located and very desirable area to establish a business and company headquarters.</p>
      <p class="p">The city is the crossroads whereby around 20,000 vehicles pass by our site each day travelling locally and between nearby towns where boom started with relevant established support for business and infrastructure. Our project has highway frontage and is 100 yards away from the bypass intersection making it the best location in the County for this type of project.</p>
    </div>
    <div class="col" style="left:25px;top:216px;width:222px">
      <p class="p">With billions invested into infrastructure in the past 5 years in and around the oil basin our project has become the beneficiary of a major new city bypass which intersects highway 85 just 100 yards south of our project, putting us on one of the busiest intersections in the region. With this rapid growth we were included into the City limits providing additional benefits to the overall success for our development including all city services.</p>
      <p class="p">Demand stems from the ongoing boom in oil and gas drilling in the area which is still in its infancy stages of life, North Dakota oil play and is expected to continue to grow well past 2050 based on obtainable reserves beneath the ground.</p>
    </div>
  </section>

  <!-- Page 5: additional location growth -->
  <section class="page row2 c1">
    <svg class="bands" viewBox="0 0 270 378" aria-hidden="true"><polygon points="270,95 270,378 250,378 250,105" fill="var(--band)"/><polygon points="0,250 0,378 18,378 18,240" fill="var(--band)"/></svg>
    <h2 class="page-title" style="top:24px">Additional location growth</h2>
    <div class="col" style="left:25px;top:52px;width:225px;color:var(--navy);font-size:8px;line-height:1.95">
      <p>Keller Energy 150 million-dollar city investment 2018</p>
      <p>North Dakota is the nation’s second-biggest oil producer</p>
      <p>County Investment. Development</p>
    </div>
    <div class="fill" role="img" aria-label="Map of the oil patch region with counties highlighted" style="left:59px;top:104px;width:151px;height:112px;background:linear-gradient(135deg,#e3d8a8,#d9b46a 45%,#e2743a 60%,#d8c98e)"></div>
    <div class="col" style="left:25px;top:226px;width:222px">
      <p class="p">Within the 100 yards of our business park, directly across the road commercial land is currently listed at of $750,000 an acre at Harbor Commons and many more locations up to $650,000 per acre. With an advantage over other sites in terms of a better location and much lower purchase and development costs the numbers don’t lie, and we need to have pad ready to build lots to offer the market.</p>
      <p class="p">Traffic north, south, east and west will have to travel right by our site making it the second busiest intersection in the region, giving us the best exposure to sell, promote and grow. this site can and will be the location for new business and growth, we need to develop the site now to move forward.</p>
      <p class="p">With our obvious high exposure to potential buyers through the passing traffic and lower entry price point there is no doubt our Town Center will become the place where business will want to build alongside a quality business like the Northstar Suites Extended Stay Hotel.</p>
    </div>
  </section>

  <!-- Page 6: hotel and sensitivity -->
  <section class="page row2 c2">
    <svg class="bands" viewBox="0 0 270 378" aria-hidden="true"><polygon points="270,95 270,378 250,378 250,105" fill="var(--band)"/><polygon points="0,250 0,378 18,378 18,240" fill="var(--band)"/></svg>
    <h2 class="page-title" style="top:26px;left:25px;width:240px;font-size:15.5px">The Northstar Suites Extended Stay</h2>
    <div class="col" style="left:25px;top:70px;width:222px">
      <p class="p">Northstar’s unmatched experience and leadership in the hotel industry designed a new extended stay hotel that satisfy one of the most in-demand needs of today’s business and leisure travellers.</p>
      <p class="p">Here guests will experience the very best in hotel and home. Its flexible spaces, stylish design, and brand signature elements come together to create an enriching extended stay experience for your guests, while building loyalty and repeat bookings for your hotel.</p>
    </div>
    <h3 class="page-title" style="top:109px;left:25px">Sensitivity Analysis</h3>
    <div class="col" style="left:25px;top:131px;width:222px">
      <p class="p">Sensitivity analysis is based on sales of the full site. (45 saleable acres)<br>Our numbers below don’t include revenue from build to suit projects or potential income stream from construction of the motel and various projects that could be developed on this 60-acre site. <em>These costs are only shown as estimates at this stage.</em></p>
    </div>
    <table class="sens">
      <tr><th>Estimated Projections</th><th>Projected</th><th>Best Scenario</th><th>Worst Scenario</th></tr>
      <tr><td>Average sale per acre (45)</td><td>$450,000</td><td>$500,000</td><td>$350,000</td></tr>
      <tr><td>Total Sales</td><td>$20,250,000</td><td>$22,500,000</td><td>$15,750,000</td></tr>
      <tr><td>Projected Expenses</td><td></td><td></td><td></td></tr>
      <tr><td>Engineers</td><td>$250,000</td><td>$250,000</td><td>$300,000</td></tr>
      <tr><td>Estimated Site Development Works</td><td>$2,400,000</td><td>$2,000,000</td><td>$3,500,000</td></tr>
      <tr><td>Site Licences / Permits</td><td>$450,000</td><td>$350,000</td><td>$500,000</td></tr>
      <tr><td>Additional Signage, Marketing</td><td>$20,000</td><td>$15,000</td><td>$25,000</td></tr>
      <tr><td>Professional Fees</td><td>$135,000</td><td>$130,000</td><td>$145,000</td></tr>
      <tr><td>Attorney Contracts / Support</td><td>$45,000</td><td>$30,000</td><td>$50,000</td></tr>
      <tr><td>Realtor Commissions</td><td>$1,000,000</td><td>$900,000</td><td>$1,200,000</td></tr>
      <tr><td>Property Payout</td><td>$7,200,000</td><td>$7,200,000</td><td>$7,200,000</td></tr>
      <tr><td>Estimated Projected Full Costs</td><td>$11,500,000</td><td>$10,815,000</td><td>$12,920,000</td></tr>
      <tr><td>Estimated Projected Per Acre Costs</td><td>$255,000</td><td>$240,000</td><td>$287,000</td></tr>
      <tr><td>Estimated Total Projected Profit</td><td>$8,750,000</td><td>$11,685,000</td><td>$2,830,000</td></tr>
      <tr><td>Estimated Profit Each Partner</td><td>$4,375,000</td><td>$5,842,500</td><td>$1,415,000</td></tr>
    </table>
    <div class="col" style="left:25px;top:344px;width:222px"><p class="p">This investment may offer an opportunity for a visa into the USA however you will need to undertake your own inquires</p></div>
  </section>

  <!-- Page 7: team -->
  <section class="page row2 c3">
    <svg class="bands" viewBox="0 0 270 378" aria-hidden="true"><polygon points="270,95 270,378 250,378 250,105" fill="var(--band)"/><polygon points="0,250 0,378 18,378 18,240" fill="var(--band)"/></svg>
    <h2 class="page-title" style="top:27px">About Our Quality Team</h2>
    <div class="col" style="left:24px;top:50px;color:var(--title);font-size:8.5px;font-style:italic">Owner - Martin Hale</div>
    <div class="col" style="left:24px;top:68px;font-size:4.3px;font-style:italic;color:#333">I am an investor always seeking great value opportunities.</div>
    <div class="fill" role="img" aria-label="Photograph of a town main street at dusk" style="left:24px;top:85px;width:106px;height:113px;background:linear-gradient(180deg,#2a4f9a,#4f78b8 45%,#6a5346 75%,#3c3a40)"></div>
    <div class="fill" role="img" aria-label="Photograph of a town main street by day" style="left:139px;top:85px;width:106px;height:113px;background:linear-gradient(180deg,#9db3cf,#c7d3e0 45%,#8b7a6c 75%,#6d6866)"></div>
    <div class="col" style="left:24px;top:208px;color:var(--title);font-size:8.3px;font-style:italic">Our Crestline Engineering Design and Planning Team</div>
    <div class="col" style="left:25px;top:227px;width:222px">
      <p class="p">From planning to conceptual design to construction services, our planning department understands the innovative solutions needed for your project needs. Our planners collaborate with other design professions to create innovative solutions for planning projects and other design needs. Crestline designs with nature in mind and creating sustainable solutions to each unique and individual design requirement. Our pursuit is to bring the public a service with solid goals and concepts by challenging old convention and implementing new life-giving communities and spaces.</p>
      <p class="p">We have experience and capabilities in conceptual project development, master planning, feasibility studies, park and recreational design, urban and land planning.</p>
    </div>
  </section>

  <!-- Page 8: conclusion -->
  <section class="page row2 c4">
    <svg class="bands" viewBox="0 0 270 378" aria-hidden="true"><polygon points="270,95 270,378 250,378 250,105" fill="var(--band)"/><polygon points="0,250 0,378 18,378 18,240" fill="var(--band)"/></svg>
    <h2 class="page-title" style="top:27px">In Conclusion</h2>
    <div class="col" style="left:25px;top:53px;width:222px">
      <p class="p">This is a solid project located in the oil basin on top of the most cost-effective oil reserves anywhere in the region, centrally located for business and with highway frontage and now with the new Bypass intersection at our doorstep, it creates an incredible opportunity.</p>
    </div>
    <div class="fill" role="img" aria-label="Annotated aerial map showing the site, downtown, bypass, airport and traffic counts" style="left:25px;top:84px;width:212px;height:125px;background:linear-gradient(135deg,#6f7a5e,#9a9a82 40%,#7d846c 70%,#a7a58f)"></div>
    <div class="col" style="left:25px;top:223px;width:222px">
      <p class="p">I would love to have you come on board as partner, our focus is pushing hard and fast to take advantage of the window of opportunity with the weather in March next year and have everything ready to roll and have lots ready for sale before August 2019.</p>
    </div>
    <div class="contact"><em>Please send all questions and all joint venture proposals to:</em><br>Martin Hale<br>+61 400 555 018<br>email: martin.hale@example.com<br>Australia</div>
  </section>

</main>
</body>
</html>
```